Redesign of existing business card

I would like the "signage" attachment converted into a business card. This needs to be double sided aswell, keeping the phone number and names on the front, and the email + website on the back.

Second attachment is the current business card design.

Larger font for contact details is required.

Must keep to original color themes (electric blue, silver/grey etc)

Back of the card to have blue background with white writing.

Industry/Entity Type

Business

Contact Information for Business Card

Refer to existing design from attachments

Requirements
Must have
• Refer to existing design from attachments
Nice to have

```html
<!DOCTYPE html>
<html lang="en">
<head>
<meta charset="utf-8">
<title>Voltline Electro Services – Business Card</title>
<link rel="stylesheet" href="https://fonts.googleapis.com/css2?family=Arimo:wght@400;700&display=swap">
<style>
  :root {
    --electric-blue: #1f1ff5;
    --deep-blue: #1414c8;
    --silver: #8a8d93;
    --ink: #4a4a4f;
    --paper: #ffffff;
    --stage: #3b3b3d;
  }
  * { box-sizing: border-box; margin: 0; padding: 0; }
  html, body { width: 1200px; height: 950px; overflow: hidden; }
  body {
    background: var(--stage);
    font-family: "Arimo", Arial, sans-serif;
    position: relative;
  }
  .card {
    position: absolute;
    left: 250px;
    width: 700px;
    height: 400px;
    overflow: hidden;
  }
  .card--back { top: 50px; background: var(--electric-blue); }
  .card--front { top: 500px; background: var(--paper); }

  .brand {
    position: absolute;
    display: flex;
    align-items: center;
    gap: 16px;
    font-weight: 700;
    text-transform: uppercase;
  }
  .brand__dot {
    width: 62px; height: 62px;
    border-radius: 50%;
    border: 6px solid currentColor;
    flex: none;
  }
  .brand__name { line-height: 1; }
  .brand__name .brand__main { display: block; font-size: 52px; letter-spacing: 2px; }
  .brand__name .brand__sub { display: block; font-size: 21px; letter-spacing: 1px; margin-top: 4px; }

  .card--back .brand { left: 150px; top: 140px; color: var(--paper); }
  .card--back .web {
    position: absolute; left: 0; right: 0; top: 300px;
    text-align: center; color: var(--paper);
    font-size: 17px; letter-spacing: 3px;
  }

  .card--front .brand { right: 70px; top: 70px; color: var(--electric-blue); }
  .card--front .brand__dot { width: 50px; height: 50px; border-width: 5px; }
  .card--front .brand__main { font-size: 42px; }
  .card--front .brand__sub { font-size: 17px; }

  .side-band { position: absolute; left: 0; top: 0; }

  .contact {
    position: absolute; left: 135px; top: 238px;
    color: var(--ink);
  }
  .contact__name { color: var(--electric-blue); font-weight: 700; font-size: 24px; text-transform: uppercase; }
  .contact__role { color: var(--silver); font-size: 18px; margin-top: 4px; }
  .contact__line { font-size: 19px; margin-top: 9px; }
  .contact__role + .contact__line { margin-top: 14px; }
</style>
</head>
<body>

<section class="card card--back" aria-label="Card back">
  <div class="brand">
    <span class="brand__dot"></span>
    <span class="brand__name"><span class="brand__main">Voltline</span><span class="brand__sub">Electro Services</span></span>
  </div>
  <p class="web">www.voltlineelectro.com.au</p>
</section>

<section class="card card--front" aria-label="Card front">
  <div class="brand">
    <span class="brand__dot"></span>
    <span class="brand__name"><span class="brand__main">Voltline</span><span class="brand__sub">Electro Services</span></span>
  </div>

  <svg class="side-band" width="140" height="400" viewBox="0 0 140 400" aria-hidden="true">
    <polygon points="0,0 18,0 18,205 98,245 98,400 0,400" fill="var(--electric-blue)"/>
    <polyline points="30,0 30,198 112,240 112,400" fill="none" stroke="var(--silver)" stroke-width="8"/>
    <g fill="#fff">
      <!-- person -->
      <circle cx="55" cy="262" r="7"/>
      <path d="M42 282 q13 -16 26 0 z"/>
      <!-- phone -->
      <path d="M44 310 h22 v4 h-6 v-2 h-10 v2 h-6 z"/>
      <rect x="46" y="316" width="18" height="12" rx="2"/>
      <!-- mail -->
      <rect x="44" y="340" width="22" height="15" rx="1"/>
      <path d="M44 340 l11 9 l11 -9" fill="none" stroke="var(--electric-blue)" stroke-width="2"/>
      <!-- globe -->
      <circle cx="55" cy="378" r="10"/>
      <path d="M45 378 h20 M55 368 v20" stroke="var(--electric-blue)" stroke-width="2"/>
    </g>
  </svg>

  <div class="contact">
    <p class="contact__name">Sam Hartley</p>
    <p class="contact__role">President</p>
    <p class="contact__line">555 0192 4470</p>
    <p class="contact__line">sam@voltlineelectro.com</p>
    <p class="contact__line">www.voltlineelectro.com</p>
  </div>
</section>

</body>
</html>
```